M Website

We need a website design for a construction plant company. You may use a combination of our photos and the stock images. See the logo for company colours. It also be of great value to see moving pictures like the ones on the link: https://www.quindellworks.co.za/copy-of-about-us. See our uploaded files for content.

Target Market(s)

Construction

Number of Pages Required

5+ page

```html
<!DOCTYPE html>
<html lang="en">
<head>
<meta charset="utf-8">
<title>Kestrel Logistics &amp; Plant Hire</title>
<link rel="stylesheet" href="https://fonts.googleapis.com/css2?family=Raleway:wght@400;500;600;700&display=swap">
<style>
:root{
  --yellow:#f6b40c;
  --yellow-soft:#fbd15a;
  --dark:#3c3c3c;
  --footer:#2a2a2a;
  --ink:#333333;
  --muted:#6b6b6b;
  --line:#e3e3e3;
  --tile:#f1f1f1;
  --white:#ffffff;
}
*{box-sizing:border-box;margin:0;padding:0}
html,body{width:1200px;height:4128px;overflow:hidden}
body{position:relative;font-family:"Raleway",sans-serif;color:var(--ink);background:var(--white)}
.abs{position:absolute}
.photo{position:absolute}

/* header */
.site-header{position:absolute;left:0;top:0;width:1200px;height:116px;background:var(--white)}
.brand{position:absolute;left:80px;top:30px;display:flex;align-items:center;gap:10px}
.brand-dot{width:44px;height:44px;border-radius:50%;background:var(--yellow)}
.brand-name{font-size:26px;font-weight:700;color:var(--ink);line-height:1}
.nav{position:absolute;left:542px;top:52px;display:flex;gap:46px;font-size:15px;color:var(--muted)}
.nav a{color:inherit;text-decoration:none;position:relative}
.nav a.active{color:var(--ink);font-weight:600}
.nav a.active::after{content:"";position:absolute;left:0;right:0;top:46px;height:4px;background:var(--yellow)}
.nav-search{position:absolute;left:1104px;top:53px}

/* hero */
.hero{position:absolute;left:0;top:116px;width:1200px;height:572px;overflow:hidden}
.hero-photo{left:0;top:0;width:1200px;height:572px;background:linear-gradient(160deg,#8a6a3a 0%,#5a4c3a 35%,#7d7468 60%,#a59c90 100%)}
.hero-title{position:absolute;left:0;width:1200px;top:210px;text-align:center;color:var(--white);font-size:56px;font-weight:500}
.hero-sub{position:absolute;left:0;width:1200px;top:282px;text-align:center;color:var(--white);font-size:27px}
.hero-play{position:absolute;left:581px;top:330px}
.hero-curve{position:absolute;left:0;top:430px}

/* values */
.value{position:absolute;top:751px;width:185px;height:94px;background:var(--tile);display:flex;align-items:center;justify-content:center;gap:12px;font-size:18px;color:var(--ink)}
.value.active{background:var(--yellow)}

/* overview */
.overview-frame{left:80px;top:916px;width:470px;height:300px;background:var(--yellow)}
.overview-photo{left:96px;top:936px;width:479px;height:308px;background:linear-gradient(180deg,#5f95cf 0%,#9cc3e6 45%,#c9a77a 70%,#a97f4d 100%)}
.section-heading{font-size:33px;font-weight:500;color:var(--ink)}
.rule{position:absolute;width:44px;height:4px;background:var(--yellow)}
.overview-title{position:absolute;left:663px;top:945px}
.overview-text{position:absolute;left:663px;top:1024px;width:340px;font-size:12.5px;line-height:17px;color:var(--muted)}
.btn{position:absolute;display:flex;align-items:center;justify-content:center;background:var(--yellow);color:var(--white);border-radius:22px;font-size:14px;font-weight:600}
.scroll-track{left:1113px;top:960px;width:3px;height:220px;background:var(--line)}
.scroll-thumb{left:1113px;top:1040px;width:4px;height:80px;background:var(--yellow)}

/* services */
.services{position:absolute;left:0;top:1326px;width:1200px;height:488px;background:var(--dark)}
.band-title{position:absolute;left:0;width:1200px;text-align:center;font-size:33px;font-weight:500}
.service-card{position:absolute;top:119px;width:245px;height:292px;background:var(--white);border:2px solid #eaeaea}
.service-photo{position:absolute;left:8px;top:8px;width:225px;height:138px}
.service-icon{position:absolute;left:101px;top:126px;width:34px;height:34px;border-radius:50%;background:var(--white);display:flex;align-items:center;justify-content:center}
.service-name{position:absolute;left:0;width:241px;top:166px;text-align:center;font-size:15px;color:var(--ink)}
.service-text{position:absolute;left:16px;width:209px;top:196px;text-align:center;font-size:11px;line-height:14px;color:var(--muted)}
.read-more{position:absolute;left:0;width:241px;top:250px;text-align:center;font-size:11px;color:var(--ink)}

/* projects */
.project{position:absolute;width:327px;height:237px}
.project-overlay{background:var(--yellow-soft);color:var(--white);display:flex;flex-direction:column;align-items:center;justify-content:center;text-align:center}
.project-overlay h3{font-size:20px;font-weight:500;margin-bottom:6px}
.project-overlay p{font-size:12px;line-height:15px;width:200px}
.project-overlay span{font-size:12px;margin-top:4px}

/* blogs */
.blogs{position:absolute;left:0;top:2634px;width:1200px;height:516px;background:var(--dark)}
.blog-card{position:absolute;top:2763px;width:333px;height:429px;background:var(--white);box-shadow:0 2px 8px rgba(0,0,0,.18)}
.blog-photo{position:absolute;left:16px;top:16px;width:301px;height:212px}
.blog-title{position:absolute;left:38px;top:249px;font-size:19px;font-weight:600;color:var(--ink)}
.blog-date{position:absolute;right:20px;top:253px;font-size:12px;color:var(--muted)}
.blog-text{position:absolute;left:38px;top:281px;width:270px;font-size:12px;line-height:16px;color:var(--muted)}
.blog-meta{position:absolute;left:38px;top:348px;width:270px;display:flex;align-items:center;font-size:12px;color:var(--muted)}
.blog-meta .link{margin-right:auto}
.blog-meta .count{display:flex;align-items:center;gap:5px;margin-left:16px}

/* clients */
.client{position:absolute;top:3393px;width:181px;height:130px;background:var(--tile);display:flex;align-items:center;justify-content:center;font-size:20px;font-weight:700;color:#2e2e2e}
.newsletter-sub{position:absolute;left:0;width:1200px;top:3610px;text-align:center;font-size:13px;color:var(--muted)}
.newsletter-input{position:absolute;left:325px;top:3646px;width:561px;height:40px;border-radius:20px;background:#f3f3f3;font-size:12px;font-style:italic;color:var(--muted);padding:12px 26px}
.newsletter-btn{left:770px;top:3646px;width:116px;height:40px;border-radius:0 20px 20px 0;font-size:12px}

/* footer */
.footer{position:absolute;left:0;top:3700px;width:1200px;height:428px;background:var(--footer);color:#d8d8d8}
.footer-curve{position:absolute;left:0;top:3690px}
.footer-brand{position:absolute;left:69px;top:3832px;display:flex;align-items:center;gap:10px}
.footer-brand .brand-name{color:var(--white);font-size:24px}
.footer-about{position:absolute;left:69px;top:3930px;width:260px;font-size:12px;line-height:16px;color:#d8d8d8}
.footer-readmore{position:absolute;left:69px;top:3998px;font-size:12px;color:#d8d8d8}
.footer-head{position:absolute;top:3850px;font-size:14px;font-weight:600;color:var(--white)}
.footer-head::after{content:"";position:absolute;left:0;top:24px;width:34px;height:2px;background:var(--yellow)}
.quick-links{position:absolute;left:405px;top:3898px;list-style:none;font-size:12px;line-height:18px}
.quick-links li::before{content:"";display:inline-block;width:4px;height:4px;border-radius:50%;background:var(--yellow);margin-right:10px;vertical-align:middle}
.contact-list{position:absolute;left:644px;top:3896px;font-size:12px;line-height:15px;display:grid;grid-template-columns:78px 180px;column-gap:8px}
.contact-list dt{text-align:right;color:#bdbdbd}
.contact-list dd{color:#e2e2e2}
.subscribe-text{position:absolute;left:889px;top:3898px;font-size:12px;color:var(--white)}
.subscribe-input{position:absolute;left:896px;top:3934px;width:150px;height:26px;border:1px solid #777;border-radius:13px 0 0 13px;font-size:11px;color:#ccc;padding:6px 10px}
.subscribe-btn{left:1046px;top:3934px;width:72px;height:26px;border-radius:0 13px 13px 0;font-size:11px}
.footer-rule{position:absolute;left:69px;top:4058px;width:1062px;height:1px;background:#4a4a4a}
.copyright{position:absolute;left:80px;top:4080px;font-size:12px;color:#cfcfcf;display:flex;gap:18px}
.socials{position:absolute;left:1060px;top:4078px;display:flex;gap:10px}
.socials span{width:20px;height:20px;border-radius:4px;background:#4f7cc7}
</style>
</head>
<body>

<header class="site-header">
  <div class="brand"><span class="brand-dot"></span><span class="brand-name">Kestrel</span></div>
  <nav class="nav">
    <a class="active" href="#">Home</a>
    <a href="#">About us</a>
    <a href="#">Services</a>
    <a href="#">Projects</a>
    <a href="#">Blogs</a>
    <a href="#">Contact us</a>
  </nav>
  <svg class="nav-search" width="14" height="14" viewBox="0 0 14 14"><circle cx="6" cy="6" r="4.5" fill="none" stroke="#777" stroke-width="1.6"/><line x1="9.3" y1="9.3" x2="13" y2="13" stroke="#777" stroke-width="1.6"/></svg>
</header>

<section class="hero">
  <div class="photo hero-photo" role="img" aria-label="Close-up of a yellow loader bucket and tyre on a dusty construction site"></div>
  <h1 class="hero-title">Transforming</h1>
  <p class="hero-sub">our clients vision into reality</p>
  <svg class="hero-play" width="38" height="38" viewBox="0 0 38 38"><circle cx="19" cy="19" r="17" fill="none" stroke="#fff" stroke-width="2.5"/><path d="M15 12 L27 19 L15 26 Z" fill="#fff"/></svg>
  <svg class="hero-curve" width="1200" height="142" viewBox="0 0 1200 142">
    <path d="M0 30 C 300 110, 800 110, 1200 20 L1200 142 L0 142 Z" fill="#f6b40c"/>
    <path d="M0 50 C 320 135, 820 130, 1200 48 L1200 142 L0 142 Z" fill="#ffffff"/>
  </svg>
</section>

<div class="value" style="left:80px">
  <svg width="24" height="24" viewBox="0 0 24 24"><circle cx="12" cy="12" r="10" fill="none" stroke="#333" stroke-width="2"/><path d="M7 12 L11 16 L17 8" fill="none" stroke="#333" stroke-width="2"/></svg>Integrity</div>
<div class="value" style="left:292px">
  <svg width="24" height="24" viewBox="0 0 24 24"><circle cx="12" cy="12" r="10" fill="none" stroke="#333" stroke-width="2"/><path d="M7 12 L11 16 L17 8" fill="none" stroke="#333" stroke-width="2"/></svg>Accountability</div>
<div class="value active" style="left:506px">
  <svg width="24" height="24" viewBox="0 0 24 24"><circle cx="12" cy="12" r="10" fill="none" stroke="#333" stroke-width="2"/><path d="M7 12 L11 16 L17 8" fill="none" stroke="#333" stroke-width="2"/></svg>Capability</div>
<div class="value" style="left:718px">
  <svg width="24" height="24" viewBox="0 0 24 24"><circle cx="12" cy="12" r="10" fill="none" stroke="#333" stroke-width="2"/><path d="M7 12 L11 16 L17 8" fill="none" stroke="#333" stroke-width="2"/></svg>Adaptability</div>
<div class="value" style="left:933px">
  <svg width="24" height="24" viewBox="0 0 24 24"><circle cx="12" cy="12" r="10" fill="none" stroke="#333" stroke-width="2"/><path d="M7 12 L11 16 L17 8" fill="none" stroke="#333" stroke-width="2"/></svg>Ethics</div>

<section class="overview">
  <div class="photo overview-frame"></div>
  <div class="photo overview-photo" role="img" aria-label="Orange wheel loader working on a sand mound under a blue sky"></div>
  <h2 class="section-heading overview-title">Company Overview</h2>
  <span class="rule" style="left:663px;top:996px"></span>
  <p class="overview-text">Kestrel Logistics and Plant Hire (Pty) Ltd is a Black Woman owned Construction and Plant Hire company operating mainly from the Kestrel head office in Riverbend (Oakridge) Northvale. Kestrel Logistics and Plant Hire (Pty) Ltd was established in 2014, and has worked in various municipal jurisdictions within South Africa.</p>
  <a class="btn" style="left:663px;top:1181px;width:176px;height:41px">Read More</a>
  <div class="abs scroll-track"></div>
  <div class="abs scroll-thumb"></div>
</section>

<section class="services">
  <h2 class="band-title" style="top:36px;color:#fff">Our Serices</h2>
  <span class="rule" style="left:578px;top:86px"></span>

  <article class="service-card" style="left:74px">
    <div class="photo service-photo" role="img" aria-label="Flooded road with stormwater running over the tarmac" style="background:linear-gradient(180deg,#7d8a94,#b8b2a6)"></div>
    <div class="service-icon"><svg width="16" height="16" viewBox="0 0 16 16"><rect x="2" y="9" width="12" height="4" fill="#555"/><rect x="5" y="4" width="6" height="5" fill="#555"/></svg></div>
    <h3 class="service-name">Roads &amp; Stormwater</h3>
    <p class="service-text">Lorem Ipsum is simply dummy text of the printing and typesetting industry is simply dummy text</p>
    <p class="read-more">Read More &#8250;</p>
  </article>
  <article class="service-card" style="left:339px">
    <div class="photo service-photo" role="img" aria-label="Worker in blue overalls fitting a water pipe in a trench" style="background:linear-gradient(180deg,#4d6f9a,#8c7a62)"></div>
    <div class="service-icon"><svg width="16" height="16" viewBox="0 0 16 16"><rect x="7" y="2" width="2" height="12" fill="#555"/><rect x="2" y="7" width="12" height="2" fill="#555"/></svg></div>
    <h3 class="service-name">Water Infrastructure</h3>
    <p class="service-text">Lorem Ipsum is simply dummy text of the printing and typesetting industry is simply dummy text</p>
    <p class="read-more">Read More &#8250;</p>
  </article>
  <article class="service-card" style="left:608px">
    <div class="photo service-photo" role="img" aria-label="Sanitation pipe laid in a dug trench" style="background:linear-gradient(180deg,#8a5a3c,#b98a62)"></div>
    <div class="service-icon"><svg width="16" height="16" viewBox="0 0 16 16"><rect x="5" y="2" width="6" height="12" rx="2" fill="#555"/></svg></div>
    <h3 class="service-name">Sanitation Infrastructure</h3>
    <p class="service-text">Lorem Ipsum is simply dummy text of the printing and typesetting industry is simply dummy text</p>
    <p class="read-more">Read More &#8250;</p>
  </article>
  <article class="service-card" style="left:881px">
    <div class="photo service-photo" role="img" aria-label="House under construction with scaffolding against a blue sky" style="background:linear-gradient(180deg,#6d9fd6,#c2b8a8)"></div>
    <div class="service-icon"><svg width="16" height="16" viewBox="0 0 16 16"><path d="M2 8 L8 3 L14 8 L14 14 L2 14 Z" fill="#555"/></svg></div>
    <h3 class="service-name">Housing</h3>
    <p class="service-text">Lorem Ipsum is simply dummy text of the printing and typesetting industry is simply dummy text</p>
    <p class="read-more">Read More &#8250;</p>
  </article>
</section>

<section class="projects">
  <h2 class="band-title section-heading" style="top:1876px">Our Projects</h2>
  <div class="photo project" style="left:80px;top:1954px;background:linear-gradient(150deg,#c98a46,#8a6a4c)" role="img" aria-label="Orange excavator digging soil"></div>
  <div class="photo project project-overlay" style="left:435px;top:1954px">
    <h3>Roads &amp; Stormwater</h3>
    <p>Lorem Ipsum is simply dummy text of the printing and typesetting industry.</p>
    <span>Read More &#8250;</span>
  </div>
  <div class="photo project" style="left:793px;top:1954px;background:linear-gradient(160deg,#a06a3c,#d9a04a)" role="img" aria-label="Excavator beside a building frame under construction"></div>
  <div class="photo project" style="left:80px;top:2224px;background:linear-gradient(160deg,#5a5a5a,#a19a8e)" role="img" aria-label="Workers in safety vests beside a truck with traffic cones"></div>
  <div class="photo project" style="left:435px;top:2224px;background:linear-gradient(160deg,#6e5a48,#bfae98)" role="img" aria-label="Close-up of a machine part on a work site"></div>
  <div class="photo project" style="left:793px;top:2224px;background:linear-gradient(180deg,#b8d0e0,#4f7a3e)" role="img" aria-label="Yellow excavator in front of green trees"></div>
  <a class="btn" style="left:517px;top:2524px;width:179px;height:41px">View More</a>
</section>

<section class="blogs">
  <h2 class="band-title" style="top:52px;color:#fff">Our Blogs</h2>
  <span class="rule" style="left:578px;top:102px"></span>
</section>
<article class="blog-card" style="left:69px">
  <div class="photo blog-photo" role="img" aria-label="Excavator working inside a deep earth trench" style="background:linear-gradient(180deg,#d4c2b0,#8a4f34)"></div>
  <h3 class="blog-title">Blog # 1</h3><span class="blog-date">Feb.15.2019</span>
  <p class="blog-text">Lorem Ipsum is simply dummy text of the printing and typesetting industry.</p>
  <div class="blog-meta"><span class="link">Read Full Article</span>
    <span class="count"><svg width="14" height="12" viewBox="0 0 14 12"><path d="M7 11 L1.5 5.5 A3 3 0 0 1 7 2.5 A3 3 0 0 1 12.5 5.5 Z" fill="none" stroke="#777" stroke-width="1.3"/></svg>35</span>
    <span class="count"><svg width="14" height="12" viewBox="0 0 14 12"><path d="M2 1 H12 V8 H6 L3 11 V8 H2 Z" fill="none" stroke="#777" stroke-width="1.3"/></svg>20</span></div>
</article>
<article class="blog-card" style="left:435px">
  <div class="photo blog-photo" role="img" aria-label="Loader bucket silhouetted against a sunset sky" style="background:linear-gradient(180deg,#e7b26a,#5a4032)"></div>
  <h3 class="blog-title">Blog # 2</h3><span class="blog-date">Feb.15.2019</span>
  <p class="blog-text">Lorem Ipsum is simply dummy text of the printing and typesetting industry.</p>
  <div class="blog-meta"><span class="link">Read Full Article</span>
    <span class="count"><svg width="14" height="12" viewBox="0 0 14 12"><path d="M7 11 L1.5 5.5 A3 3 0 0 1 7 2.5 A3 3 0 0 1 12.5 5.5 Z" fill="none" stroke="#777" stroke-width="1.3"/></svg>40</span>
    <span class="count"><svg width="14" height="12" viewBox="0 0 14 12"><path d="M2 1 H12 V8 H6 L3 11 V8 H2 Z" fill="none" stroke="#777" stroke-width="1.3"/></svg>23</span></div>
</article>
<article class="blog-card" style="left:798px">
  <div class="photo blog-photo" role="img" aria-label="Excavator next to a steel building frame" style="background:linear-gradient(180deg,#9cc0e0,#c49848)"></div>
  <h3 class="blog-title">Blog # 3</h3><span class="blog-date">Feb.15.2019</span>
  <p class="blog-text">Lorem Ipsum is simply dummy text of the printing and typesetting industry.</p>
  <div class="blog-meta"><span class="link">Read Full Article</span>
    <span class="count"><svg width="14" height="12" viewBox="0 0 14 12"><path d="M7 11 L1.5 5.5 A3 3 0 0 1 7 2.5 A3 3 0 0 1 12.5 5.5 Z" fill="none" stroke="#777" stroke-width="1.3"/></svg>25</span>
    <span class="count"><svg width="14" height="12" viewBox="0 0 14 12"><path d="M2 1 H12 V8 H6 L3 11 V8 H2 Z" fill="none" stroke="#777" stroke-width="1.3"/></svg>20</span></div>
</article>
<a class="btn" style="left:517px;top:3234px;width:179px;height:41px">View More</a>

<section class="clients">
  <h2 class="band-title section-heading" style="top:3318px">Our Clients</h2>
  <div class="client" style="left:80px">ORBITLINE</div>
  <div class="client" style="left:295px">VELTRAX</div>
  <div class="client" style="left:509px">IRONHOLD</div>
  <div class="client" style="left:724px">SUNWISE</div>
  <div class="client" style="left:939px">FINCHLEY</div>
</section>

<section class="newsletter">
  <h2 class="band-title section-heading" style="top:3563px">Our Clients</h2>
  <p class="newsletter-sub">Sign up with your email address to receive news and updates.</p>
  <div class="newsletter-input">Your Email Here</div>
  <a class="btn newsletter-btn">SUBMIT</a>
</section>

<footer>
  <div class="footer"></div>
  <svg class="footer-curve" width="1200" height="100" viewBox="0 0 1200 100">
    <path d="M0 0 H1200 V30 C 800 85, 350 80, 0 40 Z" fill="#ffffff"/>
    <path d="M0 40 C 350 80, 800 85, 1200 30 L1200 44 C 800 98, 350 92, 0 54 Z" fill="#f6b40c"/>
  </svg>
  <div class="footer-brand"><span class="brand-dot"></span><span class="brand-name">Kestrel</span></div>
  <p class="footer-about">Lorem Ipsum is simply dummy text of the printing and typesetting industry. Lorem Ipsum has been the industry's standard dummy text ever since the 1500s.</p>
  <p class="footer-readmore">Read More &#8250;</p>

  <h4 class="footer-head" style="left:405px">Quick Link</h4>
  <ul class="quick-links"><li>Home</li><li>About</li><li>Services</li><li>Projects</li><li>Blogs</li><li>Contact Us</li></ul>

  <h4 class="footer-head" style="left:644px">Quick Contact</h4>
  <dl class="contact-list">
    <dt>Headoffice :</dt><dd>PO Box 418, Crestview, 2210<br>12 Marula Lane, Oakridge,<br>Riverbend, 2214</dd>
    <dt>Branch :</dt><dd>Unit 7, Hillside Centre<br>Stonebridge 9410</dd>
    <dt>Phone :</dt><dd>+27 80 00 123 4567</dd>
    <dt>Fax :</dt><dd>086 000 2233</dd>
    <dt>Email :</dt><dd>info@kestrelplant.co.za</dd>
  </dl>

  <h4 class="footer-head" style="left:889px">Subscribe</h4>
  <p class="subscribe-text">Subscribe For Our Newsletter</p>
  <div class="subscribe-input">Email Address</div>
  <a class="btn subscribe-btn">Subscribe</a>

  <div class="footer-rule"></div>
  <div class="copyright"><span>Copyright &copy; 2019 Kestrel Logistic &amp; Plant Hire . All Right Reserve</span><span>|</span><span>Privacy Policy</span><span>|</span><span>Terms &amp; Conditions</span></div>
  <div class="socials"><span></span><span></span><span style="background:#c43a3a"></span><span style="background:#4a9fd8"></span></div>
</footer>

</body>
</html>
```